Law Office needs logo and desing for letterhead and envelopes

Creative yet elegant logo/for my letterhead and envelopes for law office that does wills, trusts, trust administration, tax planning, business planning. No limits on color or creativity.

Law Offices of Peter M. Holloway
48217 Maple Crest Avenue, Suite 207
Woodland Hills, CA 91872
p: 818.555.0142 f: 818.555.0187
e: pholloway@trevmarlaw.com

widows, trust fund beneficiaries, retirees

Business

00a88f
34b8a4
86cfc6
0692cd
33a6d7
86cae6
0555a3
3176b5
85acd3

```html
<!DOCTYPE html>
<html lang="en">
<head>
<meta charset="utf-8">
<title>Peter M. Holloway — Stationery</title>
<link rel="stylesheet" href="https://fonts.googleapis.com/css2?family=Libre+Baskerville:wght@700&family=Mulish:ital,wght@1,400&display=swap">
<style>
  :root {
    --lime: #8ee800;
    --lime-bright: #99ff00;
    --lime-deep: #66cc00;
    --ink: #111111;
    --paper: #ffffff;
    --frame: #333333;
    --sheet-edge: #9a9a9a;
  }
  * { box-sizing: border-box; margin: 0; padding: 0; }
  html, body { width: 1200px; height: 1197px; overflow: hidden; background: var(--paper); }
  .canvas {
    position: relative; width: 1200px; height: 1197px;
    border: 1px solid var(--frame); background: var(--paper);
  }
  .sheet { position: absolute; background: var(--paper); }
  .letterhead { left: 24px; top: 20px; width: 800px; height: 1158px; border: 1px solid var(--sheet-edge); }
  .envelope { left: 193px; top: 678px; width: 974px; height: 424px; border: 1px solid var(--frame); }
  .band { position: absolute; left: 0; top: 0; }
  .mark-square {
    position: absolute;
    background: radial-gradient(circle at 50% 50%, var(--lime-bright), var(--lime-deep));
  }
  .firm-name {
    position: absolute; text-align: center; white-space: nowrap;
    font-family: "Libre Baskerville", Georgia, serif; font-weight: 700;
    color: var(--lime); line-height: 1;
  }
  .firm-name .lead { display: block; line-height: 1; }
  .contact {
    position: absolute; font-family: "Mulish", "Century Gothic", sans-serif;
    font-style: italic; font-weight: 400; color: var(--ink); white-space: nowrap;
  }
  /* letterhead header */
  .letterhead .mark-square { left: 436px; top: 22px; width: 102px; height: 104px; }
  .letterhead .firm-name { left: 387px; top: 132px; width: 200px; font-size: 14px; }
  .letterhead .firm-name .lead { font-size: 7px; margin-bottom: 2px; }
  .letterhead .contact { left: 555px; top: 48px; font-size: 13px; line-height: 17.5px; }
  /* standalone identity */
  .identity .mark-square { left: 912px; top: 178px; width: 192px; height: 182px; }
  .identity .firm-name { left: 828px; top: 366px; width: 372px; font-size: 25px; }
  .identity .firm-name .lead { font-size: 12px; margin-bottom: 3px; }
  /* envelope */
  .envelope .mark-square { left: 166px; top: 231px; width: 110px; height: 106px; }
  .envelope .firm-name { left: 101px; top: 346px; width: 240px; font-size: 16px; }
  .envelope .firm-name .lead { font-size: 7px; margin-bottom: 2px; }
  .envelope .contact { left: 117px; top: 381px; font-size: 13px; }
</style>
</head>
<body>
<main class="canvas">
  <section class="sheet letterhead">
    <svg class="band" width="100" height="1158" viewBox="0 0 100 1158">
      <defs>
        <linearGradient id="bandFade" x1="0" y1="0" x2="0" y2="1">
          <stop offset="0" stop-color="#66cc00"/>
          <stop offset="0.48" stop-color="#99ff00"/>
          <stop offset="1" stop-color="#66cc00"/>
        </linearGradient>
      </defs>
      <polygon points="0,0 50,0 88,548 50,1158 0,1158" fill="url(#bandFade)"/>
    </svg>
    <div class="mark-square"></div>
    <div class="firm-name"><span class="lead">Law Offices of</span>PETER M. HOLLOWAY</div>
    <address class="contact">48217 Maple Crest Avenue,<br>Suite 207&nbsp; Woodland Hills, CA 91872<br>p: 818.555.0142 f: 818.555.0187<br>e: pholloway@trevmarlaw.com</address>
  </section>

  <section class="identity">
    <div class="mark-square"></div>
    <div class="firm-name"><span class="lead">Law Offices of</span>PETER M. HOLLOWAY</div>
  </section>

  <section class="sheet envelope">
    <svg class="band" width="100" height="424" viewBox="0 0 100 424">
      <defs>
        <linearGradient id="envBandFade" x1="0" y1="0" x2="0" y2="1">
          <stop offset="0" stop-color="#88ee00"/>
          <stop offset="0.45" stop-color="#99ff00"/>
          <stop offset="1" stop-color="#77dd00"/>
        </linearGradient>
      </defs>
      <polygon points="0,0 84,0 97,182 82,424 0,424" fill="url(#envBandFade)"/>
    </svg>
    <div class="mark-square"></div>
    <div class="firm-name"><span class="lead">Law Offices of</span>PETER M. HOLLOWAY</div>
    <address class="contact">48217 Maple Crest Avenue, Suite 207&nbsp; Woodland Hills, CA 91872 p: 818.555.0142 f: 818.555.0187 e: pholloway@trevmarlaw.com</address>
  </section>
</main>
</body>
</html>
```